Jewelry Business card for general purpose. Elegant and simple

We are a jewelry group with 6 stores in Mexico and 30 years in business.

We need a BC that at leats includes the name, mail, phone number and physical location (street, municipality, and county; example "Paseo Olmeda 2140", "Avenida Sotillo", "Monterrey").
Optional: we are trying to reposition the brand with the association of life-events or moments and family. Such as: birth, marriage, graduation, birthdays. Christmast, mothers day and fathers day.

We are looking for something elegant but simple

Jewelry name: "Lunetti". Email: "lunettibrillo@correo-ejemplo.mx". Phone num "4172-3095".

Target Market(s)

General business card: from suppliers to clients. One segment outstand: couples gettineg married

Industry/Entity Type

Jewelry Store

Contact Information for Business Card

Loking for something simple but elegant.

Font styles to use
Decorative
Script

Requirements
Must have
• Must have name, address, and mail.
Nice to have
• It could have jewelry pictures/design. Maybe quotes. Or general words as background . currently we have a very simple card with one ring would like to see something different.
Should not have
• Include real people.

```html
<!DOCTYPE html>
<html lang="es">
<head>
<meta charset="utf-8">
<title>Joyería Lunetti – Tarjeta de presentación</title>
<link rel="stylesheet" href="https://fonts.googleapis.com/css2?family=Open+Sans:wght@400&display=swap">
<style>
  :root {
    --page-bg: #e9e6e1;
    --card-black: #050505;
    --card-edge: #1a1a1a;
    --gold: #e0a21c;
    --gold-light: #f1d58a;
    --gold-deep: #a8802e;
    --white: #f4f4f4;
    --reflection: #2a2a2a;
  }
  * { margin: 0; padding: 0; box-sizing: border-box; }
  html, body {
    width: 1200px;
    height: 1022px;
    overflow: hidden;
    background: var(--page-bg);
  }
  .business-card {
    position: absolute;
    left: 100px;
    top: 221px;
    width: 1000px;
    height: 580px;
    border-radius: 22px;
    background:
      linear-gradient(200deg, rgba(255,255,255,0.10) 0%, rgba(255,255,255,0.03) 38%, rgba(255,255,255,0) 39%),
      var(--card-black);
    border: 1px solid var(--card-edge);
    overflow: hidden;
  }
  .brand-name {
    position: absolute;
    left: 44px;
    bottom: 40px;
    writing-mode: vertical-rl;
    transform: rotate(180deg);
    font-family: "Open Sans", sans-serif;
    font-weight: 400;
    font-size: 42px;
    letter-spacing: 3px;
    line-height: 1;
    color: var(--gold);
    white-space: nowrap;
  }

  .ring-photo {
    position: absolute;
    left: 250px;
    top: 40px;
    width: 400px;
    height: 250px;
    border-radius: 50%;
    background: radial-gradient(ellipse at 45% 45%, var(--gold-light) 0%, #d9bb6a 45%, var(--gold-deep) 80%, rgba(168,128,46,0) 100%);
  }
  .ring-reflection {
    position: absolute;
    left: 250px;
    top: 300px;
    width: 400px;
    height: 240px;
    border-radius: 50%;
    background: radial-gradient(ellipse at 45% 40%, var(--reflection) 0%, #161616 60%, rgba(5,5,5,0) 100%);
  }

  .contact-block {
    position: absolute;
    right: 60px;
    top: 50px;
    height: 460px;
    writing-mode: vertical-rl;
    transform: rotate(180deg);
    font-family: "Open Sans", sans-serif;
    font-size: 18px;
    line-height: 28px;
    color: var(--gold);
    list-style: none;
    text-align: start;
  }
  .contact-block li { display: block; white-space: nowrap; }
  .contact-icon {
    display: inline-block;
    width: 14px;
    height: 14px;
    margin-bottom: 8px;
    vertical-align: middle;
    transform: rotate(90deg);
  }
</style>
</head>
<body>
  <main class="business-card">
    <h1 class="brand-name">Joyeria Lunetti</h1>

    <div class="ring-photo" role="img" aria-label="Fotografía de un anillo de oro con espiral de diamantes"></div>
    <div class="ring-reflection" role="img" aria-label="Reflejo del anillo sobre la superficie brillante"></div>

    <ul class="contact-block">
      <li>
        <svg class="contact-icon" viewBox="0 0 14 14" aria-hidden="true">
          <path d="M3 1 L5 1 L6 4 L4.5 5 Q5.5 8 9 9.5 L10 8 L13 9 L13 11 Q12 13 10 13 Q2 11 1 3 Q1 1 3 1 Z" fill="var(--white)"/>
        </svg>
        4172-3095
      </li>
      <li>
        <svg class="contact-icon" viewBox="0 0 14 14" aria-hidden="true">
          <rect x="1" y="3" width="12" height="9" fill="none" stroke="var(--white)" stroke-width="1.4"/>
          <path d="M1 3 L7 8 L13 3" fill="none" stroke="var(--white)" stroke-width="1.4"/>
        </svg>
        lunettibrillo@correo-ejemplo.mx
      </li>
      <li>Paseo Olmeda 2140,</li>
      <li>Avenida Sotillo, Monterrey</li>
    </ul>
  </main>
</body>
</html>
```